Massage Therapy Business Card

I’d like the same exact business card (same graphics and colors) that I uploaded by R & K Designer with:
Name of the business: Bodywork by Delmar;
Delmar Hollis (Massage Therapist);
Contact: (555)-418-2073
Email: bodyworkbydelmar@quillmail.test;
IG: @Gr4in_bodywork

On the back Please add:
1. Mobile Sessions available upon request
2. Book 3 Massages, Get 4th 50% off

Target Market(s)

Adults ages 21+

Industry/Entity Type

Healthcare and Therapy

Contact Information for Business Card

The color should be different shades of blue with a logo of a male anatomy and pressure points for massages

Colors
0054AA
0677BA
7BADD7
CADEEF
E8F1F8
0094D4
00A9DD
6FCCEA
C7EBF8
E9F6FB
00AB8E
00BBA5
67D7C9
C6EFE9
E9F9F6
EB3D1F
EC4F4E
F09395
F8D3D4
FCEDEE

Requirements
Must have
• Must be Double Sided
Nice to have
• Newer Modern look with a Masculine Feel

```html
<!DOCTYPE html>
<html lang="en">
<head>
<meta charset="utf-8">
<title>Bodywork by Delmar – Business Card</title>
<link href="https://fonts.googleapis.com/css2?family=Montserrat:wght@400;500;600;700&display=swap" rel="stylesheet">
<style>
  :root {
    --page-bg: #ececec;
    --card-top: #2b80c8;
    --card-bottom: #1f4fae;
    --ink: #ffffff;
    --ink-soft: #dce9f7;
    --marker: #e8f1f8;
  }
  * { margin: 0; padding: 0; box-sizing: border-box; }
  html, body { width: 1200px; height: 800px; overflow: hidden; }
  body {
    background: var(--page-bg);
    font-family: "Montserrat", sans-serif;
    color: var(--ink);
    display: flex;
    align-items: center;
    justify-content: center;
    gap: 36px;
  }
  .card {
    position: relative;
    width: 560px;
    height: 320px;
    background: linear-gradient(160deg, var(--card-top) 0%, var(--card-bottom) 100%);
    box-shadow: 0 10px 28px rgba(0,0,0,0.22);
    overflow: hidden;
  }
  .illustration {
    position: absolute;
    border-radius: 40%;
    filter: blur(2px);
  }
  .card--back .illustration {
    left: 20px; top: 0; width: 230px; height: 320px;
    background: radial-gradient(ellipse at 55% 45%, rgba(240,90,74,0.55) 0%, rgba(95,159,230,0.55) 35%, rgba(31,79,174,0) 70%);
  }
  .card--front .illustration {
    left: 20px; top: 30px; width: 260px; height: 260px;
    background: radial-gradient(ellipse at 50% 50%, rgba(236,79,78,0.45) 0%, rgba(123,173,215,0.55) 35%, rgba(31,79,174,0) 70%);
  }
  .business {
    position: absolute;
    display: flex;
    align-items: center;
    gap: 10px;
    white-space: nowrap;
  }
  .business__marker {
    width: 30px; height: 30px;
    border-radius: 50%;
    background: var(--marker);
    flex-shrink: 0;
  }
  .business__name {
    font-size: 16px;
    font-weight: 600;
    line-height: 1.2;
  }
  .business__tagline {
    font-size: 10px;
    color: var(--ink-soft);
    letter-spacing: 0.3px;
    margin-top: 2px;
  }
  .card--back .business { left: 260px; top: 210px; }
  .card--front .business { left: 300px; top: 40px; }
  .offers {
    position: absolute;
    left: 260px; top: 110px;
    list-style: none;
    font-size: 12.5px;
    white-space: nowrap;
  }
  .offers li {
    display: flex; align-items: center; gap: 10px;
    margin-bottom: 10px;
  }
  .offers strong { font-weight: 700; }
  .offers svg { width: 16px; height: 16px; flex-shrink: 0; }
  .person { position: absolute; left: 300px; top: 115px; white-space: nowrap; }
  .person__name { font-size: 20px; font-weight: 700; }
  .person__role { font-size: 12px; color: var(--ink-soft); margin-top: 2px; }
  .contacts {
    position: absolute; left: 300px; top: 182px;
    list-style: none; font-size: 12px; font-weight: 500;
    white-space: nowrap;
  }
  .contacts li { display: flex; align-items: center; gap: 10px; margin-bottom: 9px; }
  .contacts svg { width: 15px; height: 15px; flex-shrink: 0; }
  .dot { width: 8px; height: 8px; margin: 0 3.5px; border-radius: 50%; background: var(--ink); flex-shrink: 0; }
</style>
</head>
<body>

  <section class="card card--back" aria-label="Business card back">
    <div class="illustration" role="img" aria-label="Glowing anatomical figure of a man holding his neck and lower back, spine highlighted in orange"></div>
    <ul class="offers">
      <li>
        <svg viewBox="0 0 16 16" aria-hidden="true"><path d="M8 0 L9.5 6.5 L16 8 L9.5 9.5 L8 16 L6.5 9.5 L0 8 L6.5 6.5 Z" fill="#fff"/></svg>
        <span>Mobile Sessions available upon request</span>
      </li>
      <li>
        <svg viewBox="0 0 16 16" aria-hidden="true"><path d="M8 0 L9.5 6.5 L16 8 L9.5 9.5 L8 16 L6.5 9.5 L0 8 L6.5 6.5 Z" fill="#fff"/></svg>
        <span>Book 3 Massages, <strong>Get 4th 50% off</strong></span>
      </li>
    </ul>
    <div class="business">
      <span class="business__marker" aria-hidden="true"></span>
      <div>
        <div class="business__name">Bodywork by Delmar</div>
        <div class="business__tagline">Massage Therapy Centre</div>
      </div>
    </div>
  </section>

  <section class="card card--front" aria-label="Business card front">
    <div class="illustration" role="img" aria-label="Translucent blue anatomical figure of a man bending forward, glowing pressure points at hip, knee and ankle"></div>
    <div class="business">
      <span class="business__marker" aria-hidden="true"></span>
      <div>
        <div class="business__name">Bodywork by Delmar</div>
        <div class="business__tagline">Massage Therapy Centre</div>
      </div>
    </div>
    <div class="person">
      <div class="person__name">Delmar Hollis</div>
      <div class="person__role">Massage Therapist</div>
    </div>
    <ul class="contacts">
      <li>
        <svg viewBox="0 0 16 16" aria-hidden="true"><rect x="4" y="1" width="8" height="14" rx="1.5" fill="none" stroke="#fff" stroke-width="1.4"/></svg>
        <span>(555)-418-2073</span>
      </li>
      <li>
        <svg viewBox="0 0 16 16" aria-hidden="true"><rect x="1" y="3.5" width="14" height="9.5" rx="1" fill="none" stroke="#fff" stroke-width="1.4"/><path d="M1.5 4 L8 9 L14.5 4" fill="none" stroke="#fff" stroke-width="1.4"/></svg>
        <span>bodyworkbydelmar@quillmail.test</span>
      </li>
      <li>
        <span class="dot" aria-hidden="true"></span>
        <span>@Gr4in_bodywork</span>
      </li>
    </ul>
  </section>

</body>
</html>
```